Solo consultant in research/analytics/data science space needs new business card

I need a new business card to promote my solo business as creative problem solver and consultant. I work on business projects for sales and market research and analytics, customer/market insights, and data science. I provide clients data-informed insights and ideas to enhance their businesses. My initial tagline: 'Make your data work for YOU.'

People should hire me because of my diverse background. Because of my Ph.D. in Political Science I have a strong background in research and analytics, project design and management, and communications skills. With my experience as a marketing analyst, a volunteer on non-profit projects, and currently as research consultant I have worked on projects within various industries. I also have a taste for improvisation so I enjoy thinking creatively and appreciate design thinking.

As an introduction to my background: Clients might want to hire me for many types of projects. Clients might wish to understand who their best customers are and how to characterize them. Maybe clients want to know how their customers feel about a certain product or service. Clients might want to know more about their local market area and overall industry. Clients might want to know whether their marketing programs are effective or else what drives their sales revenue. Perhaps clients want to use their data to create something useful for themselves or their customers.

One client hired me to help them decide whether to expand their services to newer customers. I gathered and analyzed information about the local area – the characteristics of people living there as well as the client’s competitors – and described trends and implications. The client was very pleased with the results and submitted them to superiors for approval to move forward.

For another client – who was looking to purchase a house in a metropolitan area – I gathered population and school data about the area. With this, I created an interactive mapping tool so they could zoom in on neighborhoods and learn more about them before they selected a neighborhood to purchase a house. They were happy with the results of my work.

When I worked as a marketing analyst for a consulting firm, a Vice President of Marketing hired us to discover whether or not the company’s marketing programs (i.e. coupons and discounts) were effective. I analyzed their data and our team discovered their marketing was indeed effective. He was very happy and used this to justify their programs to the Finance department (who thought such programs lost revenue).

- Marcus Delano Whitby, Ph.D.

Target Market(s)

Future clients and employers. The most immediate target markets will be other service providers such as consulting companies, marketing firms and ad agencies. I will also use this for meeting with clients in various industries.

Industry/Entity Type

Consulting

Contact Information for Business Card

Since it is my first real business card as a solo practitioner, I want to make an excellent first impression. I want this useful in case someone hires me to work on projects or else hire me to work within a firm or company. The card should convey competence and some creativity while also being neither stuffy nor a data geek.

Colors

Designer to choose colors to be used in the design.

Requirements
Nice to have
• Attached are the starting efforts at the card to add some color. It will be nice to use my name and descriptors on one side and tagline on the other. If anyone has better ideas, I will love to see them!

```html
<!DOCTYPE html>
<html lang="en">
<head>
<meta charset="utf-8">
<title>Marcus Delano Whitby, Ph.D. — Business Card</title>
<link rel="stylesheet" href="https://fonts.googleapis.com/css2?family=Bebas+Neue&family=Roboto:wght@400;700&display=swap">
<style>
  :root {
    --backdrop: #2b2c2f;
    --card-black: #0d0d0e;
    --card-black-soft: #1a1a1c;
    --brand-red: #c1222b;
    --brand-red-dark: #8f161d;
    --ink-white: #ffffff;
    --ink-grey: #d6d6d6;
    --rule-grey: #9a9a9a;
  }
  * { box-sizing: border-box; margin: 0; padding: 0; }
  html, body { width: 1200px; height: 900px; overflow: hidden; }
  body {
    background: var(--backdrop);
    font-family: "Roboto", Arial, sans-serif;
    position: relative;
  }
  .card {
    position: absolute;
    top: 296px;
    width: 540px;
    height: 309px;
    border-radius: 4px;
    overflow: hidden;
    background: linear-gradient(160deg, var(--card-black-soft), var(--card-black) 60%);
    box-shadow: 0 18px 40px rgba(0,0,0,.45);
  }
  .card--front { left: 40px; }
  .card--back { left: 620px; }

  /* Front */
  .name-band {
    position: absolute; left: 0; top: 0; width: 100%; height: 132px;
    background: linear-gradient(180deg, #c9262f, var(--brand-red));
  }
  .name-plate {
    position: absolute; left: 40px; top: 38px;
    background: var(--ink-white);
    padding: 6px 14px 2px;
    box-shadow: 6px 6px 0 var(--brand-red-dark);
    font-family: "Bebas Neue", "Oswald", sans-serif;
    font-weight: 400;
    font-size: 31px; letter-spacing: 1px;
    color: var(--brand-red);
    line-height: 1;
  }
  .brand-mark {
    position: absolute; right: 34px; top: 88px;
    display: flex; align-items: center; gap: 8px;
    font-family: "Bebas Neue", "Oswald", sans-serif;
    font-size: 26px; line-height: 1; letter-spacing: 1px;
    color: var(--ink-white);
  }
  .brand-mark__square { width: 12px; height: 12px; background: var(--ink-white); }
  .profile {
    position: absolute; left: 40px; top: 158px;
    color: var(--ink-grey); font-size: 12px; line-height: 1.4;
  }
  .profile__role { color: var(--ink-white); font-weight: 700; font-size: 14px; }
  .profile__handle { display: flex; align-items: center; gap: 6px; }
  .profile__dot { width: 9px; height: 9px; border-radius: 50%; background: var(--brand-red); }
  .divider {
    position: absolute; left: 262px; top: 176px;
    width: 1px; height: 74px; background: var(--rule-grey);
  }
  .contact {
    position: absolute; left: 292px; top: 204px;
    color: var(--ink-grey); font-size: 14px; line-height: 1.5;
    list-style: none;
  }

  /* Back */
  .tagline {
    position: absolute; left: 40px; top: 34px;
    font-family: "Bebas Neue", "Oswald", sans-serif;
    font-size: 42px; line-height: .92; letter-spacing: 1px;
    color: var(--ink-white);
  }
  .services {
    position: absolute; left: 286px; top: 120px;
    list-style: none;
  }
  .service {
    display: flex; align-items: center; gap: 14px;
    color: var(--ink-grey); font-size: 15px;
    height: 46px;
  }
  .service svg { width: 26px; height: 26px; flex: none; }
</style>
</head>
<body>

  <section class="card card--front" aria-label="Business card front">
    <div class="name-band"></div>
    <h1 class="name-plate">Marcus Delano Whitby, Ph.D.</h1>
    <div class="brand-mark"><span class="brand-mark__square"></span>Whitby Data</div>

    <div class="profile">
      <p class="profile__role">Consultant</p>
      <p>Lisbon, PT</p>
      <p class="profile__handle"><span class="profile__dot"></span>@MarcusWhitby70</p>
    </div>

    <div class="divider"></div>

    <ul class="contact">
      <li>+351 910 555 214</li>
      <li>MDWhitby70@mailbox.net</li>
      <li>MarcusDelanoWhitby.com</li>
    </ul>
  </section>

  <section class="card card--back" aria-label="Business card back">
    <p class="tagline">Make<br>your data<br>work<br>for you</p>

    <ul class="services">
      <li class="service">
        <svg viewBox="0 0 26 26" fill="none" stroke="#c1222b" stroke-width="2">
          <rect x="2" y="3" width="22" height="15" rx="1"/>
          <line x1="13" y1="18" x2="13" y2="23"/>
          <line x1="8" y1="23" x2="18" y2="23"/>
          <line x1="8" y1="14" x2="8" y2="11"/>
          <line x1="12" y1="14" x2="12" y2="8"/>
          <line x1="16" y1="14" x2="16" y2="10"/>
        </svg>
        Research/Analytics
      </li>
      <li class="service">
        <svg viewBox="0 0 26 26" fill="none" stroke="#c1222b" stroke-width="2">
          <path d="M6 18a7 7 0 0 1 14 0" fill="#c1222b"/>
          <line x1="2" y1="21" x2="24" y2="21"/>
          <line x1="13" y1="3" x2="13" y2="7"/>
          <line x1="4" y1="9" x2="7" y2="11"/>
          <line x1="22" y1="9" x2="19" y2="11"/>
        </svg>
        Customer Intelligence
      </li>
      <li class="service">
        <svg viewBox="0 0 26 26" fill="none" stroke="#c1222b" stroke-width="2">
          <path d="M5 2h11l5 5v17H5z"/>
          <path d="M16 2v5h5"/>
          <line x1="9" y1="12" x2="17" y2="12"/>
          <line x1="9" y1="16" x2="17" y2="16"/>
          <line x1="9" y1="20" x2="14" y2="20"/>
        </svg>
        Data Science
      </li>
    </ul>
  </section>

</body>
</html>
```